Business Card Design REAL ESTATE SALES PLEASE DESIGN MY CARD 2COLOR CARD WITH RED AS THE DOMINANT

FERNHOLM REALTY
TorLPA Lic# 04738216
RAFAEL " RAFE " MORTON Tel 555 218-3396
TorLPA Lic# 02864057 Fax 555 218-3740
Email: rafe@rafemortonhomes.net Cell 555 902-4481
47530 WREN TERRACE CALDER SPRINGS, TL 94312

RAFAEL " RAFE " MORTON
TEL: 555 218-3396 FAX 555 218-3740
Address: 47530 Wren Terrace Union City , CA
EMAIL ADDRESS: rafe@rafemortonhomes.net

```html
<!DOCTYPE html>
<html lang="en">
<head>
<meta charset="utf-8">
<title>Fernholm Realty – Business Card</title>
<link rel="stylesheet" href="https://fonts.googleapis.com/css2?family=Oswald:wght@400;700&display=swap">
<style>
  :root {
    --ink: #131112;
    --paper: #ffffff;
    --accent: #e50000;
  }
  html, body {
    margin: 0;
    padding: 0;
    width: 1200px;
    height: 705px;
    overflow: hidden;
    background: var(--paper);
  }
  .card {
    position: relative;
    width: 1200px;
    height: 705px;
    background: var(--paper);
    overflow: hidden;
    font-family: "Oswald", "Arial Narrow", sans-serif;
  }
  .brand {
    position: absolute;
    left: 84px;
    top: 180px;
    width: 470px;
    height: 330px;
  }
  .brand text {
    font-family: "Oswald", "Arial Narrow", sans-serif;
    font-weight: 700;
    fill: var(--ink);
  }
  .dark-panel {
    position: absolute;
    left: 662px;
    top: 0;
    width: 538px;
    height: 705px;
    background: var(--ink);
  }
  .icon-strip {
    position: absolute;
    left: 618px;
    top: 328px;
    width: 91px;
    height: 377px;
    background: var(--accent);
  }
  .icon {
    position: absolute;
    left: 50%;
    transform: translateX(-50%);
    fill: var(--paper);
  }
  .icon-phone { top: 34px; width: 52px; height: 52px; }
  .icon-mail { top: 136px; width: 64px; height: 46px; }
  .icon-pin { top: 228px; width: 44px; height: 60px; }
  .agent-name {
    position: absolute;
    left: 688px;
    top: 112px;
    display: flex;
    align-items: center;
    gap: 10px;
    margin: 0;
    color: var(--paper);
    font-weight: 400;
    font-size: 46px;
    line-height: 1;
    letter-spacing: 0.5px;
    white-space: nowrap;
  }
  .agent-name .marker {
    width: 0;
    height: 0;
    border-top: 25px solid transparent;
    border-bottom: 25px solid transparent;
    border-left: 42px solid var(--accent);
  }
  .contact {
    position: absolute;
    left: 735px;
    margin: 0;
    color: var(--paper);
    font-weight: 400;
    font-size: 41px;
    line-height: 1.28;
    white-space: nowrap;
  }
  .contact-phone { top: 316px; }
  .contact-email { top: 452px; font-size: 40px; }
  .contact-address { top: 534px; font-style: normal; }
</style>
</head>
<body>
<main class="card">
  <svg class="brand" viewBox="0 0 470 330" aria-label="Fernholm Realty">
    <text x="0" y="122" font-size="150" textLength="460" lengthAdjust="spacingAndGlyphs">FERNHOLM</text>
    <text x="0" y="316" font-size="226" textLength="466" lengthAdjust="spacingAndGlyphs">REALTY</text>
  </svg>

  <div class="dark-panel"></div>

  <div class="icon-strip">
    <svg class="icon icon-phone" viewBox="0 0 24 24" aria-hidden="true">
      <path d="M6.6 10.8c1.4 2.8 3.8 5.1 6.6 6.6l2.2-2.2c.3-.3.7-.4 1-.2 1.1.4 2.3.6 3.6.6.6 0 1 .4 1 1V20c0 .6-.4 1-1 1C10.6 21 3 13.4 3 4c0-.6.4-1 1-1h3.5c.6 0 1 .4 1 1 0 1.3.2 2.5.6 3.6.1.3 0 .7-.2 1z"/>
    </svg>
    <svg class="icon icon-mail" viewBox="0 0 64 46" aria-hidden="true">
      <path d="M2 2h60v42H2z" fill="none" stroke="#fff" stroke-width="4"/>
      <path d="M2 2l30 24L62 2M2 44l22-22M62 44L40 22" fill="none" stroke="#fff" stroke-width="4"/>
    </svg>
    <svg class="icon icon-pin" viewBox="0 0 44 60" aria-hidden="true">
      <path d="M22 0C9.9 0 0 9.6 0 21.6 0 37.5 22 60 22 60s22-22.5 22-38.4C44 9.6 34.1 0 22 0zm0 30a8.5 8.5 0 1 1 0-17 8.5 8.5 0 0 1 0 17z"/>
    </svg>
  </div>

  <h1 class="agent-name"><span class="marker"></span>RAFAEL " RAFE " MORTON</h1>

  <p class="contact contact-phone">555 218-3396<br>Fax: 555 218-3740</p>
  <p class="contact contact-email">rafe@rafemortonhomes.net</p>
  <address class="contact contact-address">47530 Wren Terrace.<br>Calder Springs, TL</address>
</main>
</body>
</html>
```